Flyer für Immobilienmakler
Zielgruppe
Wir, die Wendtal Immobilien GmbH, vermitteln Häuser, Wohnungen und Grundstücke, unsere Zielgruppe sind Verkäufer und Kaufinteressenten aus der Region, Immobilien zur Vermittlung gesucht
Aufgabenstellung
Unverbindliche Ersteinschätzung, Ansprechpartner vor Ort, regionale Marktkenntnis. Max. Din A 5, Immobilien zur Vermittlung gesucht.
- Flyer nur zur Immobilienvermittlung

```html
<!DOCTYPE html>
<html lang="de">
<head>
<meta charset="utf-8">
<title>Wendtal Immobilien – Flyer</title>
<link rel="stylesheet" href="https://fonts.googleapis.com/css2?family=Playfair+Display:wght@500;600&family=Arimo:wght@400;700&family=Source+Sans+3:wght@400;700&display=swap">
<style>
  :root{
    --bg:#e8e8ea;
    --paper:#ffffff;
    --green:#13a37c;
    --purple:#6e57a3;
    --lavender:#e1dded;
    --mint:#d0ede4;
    --footer-grey:#ececec;
    --ink:#262626;
    --body:#555555;
    --serif:"Playfair Display", Georgia, serif;
    --sans:"Arimo", Helvetica, Arial, sans-serif;
    --contact:"Source Sans 3", Arial, sans-serif;
  }
  *{box-sizing:border-box;margin:0;padding:0}
  html,body{width:1200px;height:1200px;overflow:hidden;background:var(--bg)}
  .flyer{position:absolute;left:204px;top:40px;width:792px;height:1120px;background:var(--paper);overflow:hidden}
  .header{position:absolute;left:0;top:0;width:100%;height:160px;background:var(--green);padding:34px 0 0 46px}
  .header h1{font-family:var(--serif);font-weight:500;color:#fff;font-size:49px;line-height:47px;letter-spacing:-0.03em}
  .photo{position:absolute;left:37px;top:184px;width:325px;height:372px;
    background:linear-gradient(180deg,#c9d9ef 0%,#e6edf6 35%,#b86a55 52%,#7f9a5a 68%,#5f7f3e 82%,#7fcfcf 100%)}
  .serif-h{font-family:var(--serif);font-weight:500;color:var(--ink);letter-spacing:-0.02em}
  .wanted-title{position:absolute;left:45px;top:583px;font-size:27px;line-height:32px}
  .wanted-intro{position:absolute;left:45px;top:672px;font-family:var(--sans);font-size:17px;color:var(--body)}
  .type-box{position:absolute;left:45px;width:317px;height:66px;display:flex;align-items:center;padding-left:10px;
    font-family:var(--sans);font-weight:700;font-size:20px;color:var(--ink)}
  .type-box svg{width:56px;height:56px;margin-right:24px;flex:none}
  .type-box.lavender{background:var(--lavender)}
  .type-box.mint{background:var(--mint)}
  .col-right{position:absolute;left:395px;width:362px}
  .col-right p{font-family:var(--sans);font-size:17px;line-height:20.7px;color:var(--body);margin-bottom:9px}
  .about{top:180px}
  .about h2{font-size:28px;line-height:32px;margin-bottom:18px}
  .service{top:458px;left:399px}
  .service h2{font-size:24px;line-height:28px;margin-bottom:14px}
  .service h3{font-family:var(--sans);font-weight:400;font-size:16px;color:var(--ink);margin-bottom:8px}
  .reasons{top:726px}
  .reasons h2{font-size:24px;line-height:28px;margin-bottom:20px}
  .reasons ul{list-style:none;padding-left:9px}
  .reasons li{position:relative;padding-left:22px;font-family:var(--sans);font-size:17px;line-height:20.7px;color:var(--body);margin-bottom:9px}
  .reasons li svg{position:absolute;left:0;top:2px;width:12px;height:12px}
  .footer-brand{position:absolute;left:0;top:964px;width:362px;height:156px;background:var(--footer-grey);
    display:flex;align-items:center;justify-content:center;gap:10px}
  .brand-mark{width:12px;height:12px;background:var(--green)}
  .brand-name{font-family:var(--serif);font-weight:500;font-size:19px;color:var(--ink)}
  .footer-contact{position:absolute;left:362px;top:964px;width:430px;height:156px;background:var(--purple);padding:20px 0 0 53px;color:#fff;font-family:var(--contact)}
  .footer-contact h2{font-family:var(--serif);font-weight:500;font-size:23px;margin-bottom:8px;letter-spacing:-0.02em}
  .footer-contact p{font-size:16px;line-height:20px}
  .footer-contact .company{font-weight:700}
  .footer-contact .gap{margin-top:6px}
</style>
</head>
<body>
<div class="flyer">
  <header class="header">
    <h1>Ihr Regionaler<br>Partner für Immobilienvermittlung</h1>
  </header>

  <div class="photo" role="img" aria-label="Foto: Landhaus mit rotem Ziegeldach, Garten und Pool unter bewölktem Himmel"></div>

  <h2 class="serif-h wanted-title">Immobilien Zur<br>Vermittlung Gesucht</h2>
  <p class="wanted-intro">Wir sind laufend auf der Suche nach:</p>

  <div class="type-box lavender" style="top:710px">
    <svg viewBox="0 0 56 56" fill="none" stroke="#1a1a1a" stroke-width="2"><path d="M6 28 L28 8 L50 28"/><path d="M12 23 V50 H44 V23"/><rect x="16" y="32" width="9" height="18"/><rect x="29" y="32" width="11" height="10"/><path d="M34.5 32 V42 M29 37 H40"/><path d="M38 14 V8 H43 V19"/></svg>
    Häusern
  </div>
  <div class="type-box mint" style="top:788px">
    <svg viewBox="0 0 56 56" fill="none" stroke="#1a1a1a" stroke-width="2"><rect x="6" y="10" width="44" height="40"/><path d="M4 10 H52 M4 50 H52"/><path d="M12 17 H20 M12 25 H20 M12 33 H20 M36 17 H44 M36 25 H44 M36 33 H44 M24 17 H32 M24 25 H32 M24 33 H32"/><rect x="24" y="40" width="8" height="10"/></svg>
    Wohnungen
  </div>
  <div class="type-box lavender" style="top:868px">
    <svg viewBox="0 0 56 56" fill="none" stroke="#1a1a1a" stroke-width="2"><path d="M6 22 Q14 12 24 18 Q34 10 42 16 Q48 14 50 22"/><path d="M4 24 H52"/><path d="M8 30 H48 L52 46 H4 Z"/><path d="M18 30 L14 46 M28 30 V46 M38 30 L42 46"/></svg>
    Grundstücken
  </div>

  <section class="col-right about">
    <h2 class="serif-h">Kompetente<br>Immobilienlösungen Vor Ort</h2>
    <p>Die Wendtal Immobilien GmbH mit Sitz in Wendtal ist Ihr zuverlässiger Ansprechpartner rund um die Vermittlung von Immobilien.</p>
    <p>Mit fundierter regionaler Marktkenntnis und persönlicher Betreuung unterstützen wir Eigentümer, Käufer, Verkäufer sowie Mietinteressenten.</p>
  </section>

  <section class="col-right service">
    <h2 class="serif-h">Unsere Leistung</h2>
    <h3>Immobilienvermittlung</h3>
    <p>Ob Verkauf oder Vermietung – wir kümmern uns zuverlässig um die Vermittlung von Häusern, Wohnungen, Grundstücken und Gebäuden.</p>
    <p>Dabei begleiten wir Sie persönlich von der ersten Beratung bis zum erfolgreichen Abschluss.</p>
  </section>

  <section class="col-right reasons">
    <h2 class="serif-h">Warum Wendtal Immobilien?</h2>
    <ul>
      <li><svg viewBox="0 0 12 12" fill="none" stroke="#6e57a3" stroke-width="2"><path d="M2 2 L6 6 L2 10 M6 2 L10 6 L6 10"/></svg>Persönlicher Ansprechpartner vor Ort</li>
      <li><svg viewBox="0 0 12 12" fill="none" stroke="#6e57a3" stroke-width="2"><path d="M2 2 L6 6 L2 10 M6 2 L10 6 L6 10"/></svg>Umfassende regionale Marktkenntnis</li>
      <li><svg viewBox="0 0 12 12" fill="none" stroke="#6e57a3" stroke-width="2"><path d="M2 2 L6 6 L2 10 M6 2 L10 6 L6 10"/></svg>Transparente und professionelle Abwicklung</li>
      <li><svg viewBox="0 0 12 12" fill="none" stroke="#6e57a3" stroke-width="2"><path d="M2 2 L6 6 L2 10 M6 2 L10 6 L6 10"/></svg>Zuverlässiger Partner für Eigentümer und Investoren</li>
    </ul>
  </section>

  <div class="footer-brand">
    <span class="brand-mark"></span>
    <span class="brand-name">Wendtal Immobilien GmbH</span>
  </div>

  <footer class="footer-contact">
    <h2>Kontakt</h2>
    <p class="company">Wendtal Immobilien GmbH</p>
    <p>84399 Wendtal, Mühlenweg 12</p>
    <p class="gap"><b>T</b>: +49 85 00 123450-0</p>
    <p><b>E</b>: kontakt@wendtal-immobilien.de</p>
  </footer>
</div>
</body>
</html>
```